Startup online payment business - Sporting / Golf, Swift Tee payment

Background:
Our business name is "Swift Tee" we provide online payments for golfing services via our website. We currently have a logo used on our website. No other design style has been developed. Our aim is to remove cash payments for service at golf clubs.

Our Key Values:
Quick and easy
Formal and polite
Fun with professional boundary
Mate-ship relationships
100% online digital

What we want from you:
Marketing design to be used on posters and stickers in a retail setting to direct customers to our online payment Chanel.
Design must incorporate attached logo, URL swifttee.com.au and our key values can act as a guide the type of design. We have used color Hex#007672 for logo background. We are open to use other colors.

Target Market(s)

Golf clubs and golf players

Industry/Entity Type

Golf Course

Font styles to use
Sans Serif

Requirements
Must have
• Directions to online payment via URL: swifttee.com.au
Nice to have
• We like the idea of the slogan: No Cash - No worries. Have attached home screen that will be available from URL link. Consideration if using mobile phone in image. Push the online payment and steps 1. Visit swifttee.com 2. Select club 3. Confirm payment
Should not have
• Cartoons

```html
<!DOCTYPE html>
<html lang="en">
<head>
<meta charset="utf-8">
<title>Swift Tee – No Cash No Worries</title>
<link href="https://fonts.googleapis.com/css2?family=Jost:wght@600;700&family=Questrial&family=Varela+Round&display=swap" rel="stylesheet">
<style>
  :root {
    --teal: #007672;
    --ink: #0a0a0a;
    --white: #ffffff;
    --sky-top: #cfeef7;
    --sky-mid: #eef8fb;
    --grass: #8fbf6a;
    --phone-body: #1d1f1f;
  }
  * { margin: 0; padding: 0; box-sizing: border-box; }
  html, body { width: 1200px; height: 750px; overflow: hidden; background: var(--white); }
  .poster {
    position: relative;
    width: 1200px;
    height: 750px;
    overflow: hidden;
    font-family: "Questrial", sans-serif;
  }
  .hero-photo {
    position: absolute;
    inset: 0 0 257px 0;
    background:
      linear-gradient(180deg, transparent 0%, transparent 72%, rgba(95,154,74,.55) 86%, var(--grass) 100%),
      linear-gradient(90deg, #9fd3ea 0%, #bfe4f3 25%, var(--sky-mid) 55%, var(--sky-top) 100%);
  }
  .headline {
    position: absolute;
    left: 620px;
    top: 20px;
    width: 560px;
    font-family: "Jost", sans-serif;
    font-weight: 700;
    color: var(--ink);
    line-height: 1;
    text-transform: uppercase;
    white-space: nowrap;
  }
  .headline-line-1 { display: block; font-size: 112px; letter-spacing: 3px; }
  .headline-line-2 { display: block; font-size: 80px; letter-spacing: 3px; margin-top: 2px; }
  .mission {
    position: absolute;
    left: 0;
    top: 410px;
    width: 548px;
    height: 84px;
    background: var(--white);
    border-radius: 0 22px 22px 0;
    padding: 5px 0 0 46px;
    font-family: "Varela Round", sans-serif;
    color: var(--teal);
    font-size: 22px;
    line-height: 23px;
    letter-spacing: 1.1px;
    font-weight: 700;
    -webkit-text-stroke: .5px var(--teal);
  }
  .info-band {
    position: absolute;
    left: 0;
    right: 0;
    bottom: 0;
    height: 257px;
    background: var(--teal);
  }
  .values {
    position: absolute;
    left: 46px;
    top: 522px;
    list-style: none;
    color: var(--white);
    font-size: 33px;
    line-height: 37.6px;
    white-space: nowrap;
  }
  .values li { display: flex; align-items: center; gap: 8px; }
  .values svg { width: 34px; height: 26px; flex: none; }
  .phone {
    position: absolute;
    left: 822px;
    top: 222px;
    width: 140px;
    height: 283px;
  }
  .phone-screen-text {
    position: absolute;
    left: 831px;
    top: 230px;
    width: 122px;
    text-align: center;
    color: var(--white);
  }
  .phone-brand {
    margin-top: 46px;
    font-family: "Jost", sans-serif;
    font-weight: 600;
    font-size: 22px;
    letter-spacing: 1px;
    white-space: nowrap;
  }
  .phone-tagline {
    margin-top: 58px;
    font-family: "Varela Round", sans-serif;
    font-weight: 700;
    -webkit-text-stroke: .4px var(--white);
    line-height: 18px;
  }
  .phone-tagline .big { display: block; font-size: 24px; line-height: 26px; }
  .phone-tagline .small { display: block; font-size: 19px; }
  .brand-mark {
    position: absolute;
    left: 686px;
    top: 548px;
    width: 400px;
    text-align: center;
    color: var(--white);
    font-family: "Jost", sans-serif;
    font-weight: 600;
    font-size: 66px;
    letter-spacing: 3px;
    line-height: 1;
    white-space: nowrap;
  }
  .visit {
    position: absolute;
    left: 630px;
    top: 666px;
    width: 520px;
    text-align: center;
    color: var(--white);
    font-family: "Varela Round", sans-serif;
    font-size: 32px;
    letter-spacing: 2.4px;
    -webkit-text-stroke: .8px var(--white);
    white-space: nowrap;
  }
</style>
</head>
<body>
<main class="poster">
  <div class="hero-photo" role="img" aria-label="Photo of a cheering golfer in a light blue polo and white cap raising a club on a sunny golf course"></div>

  <h1 class="headline">
    <span class="headline-line-1">No Cash</span>
    <span class="headline-line-2">No Worries</span>
  </h1>

  <p class="mission">Swift Tee is here to support Golf Clubs embrace new strategies for success in a rapidly changing world.</p>

  <section class="info-band"></section>

  <svg class="phone" viewBox="0 0 140 283" aria-hidden="true">
    <rect x="0" y="35" width="3" height="14" rx="1" fill="var(--phone-body)"/>
    <rect x="0" y="57" width="3" height="22" rx="1" fill="var(--phone-body)"/>
    <rect x="0" y="84" width="3" height="22" rx="1" fill="var(--phone-body)"/>
    <rect x="137" y="64" width="3" height="32" rx="1" fill="var(--phone-body)"/>
    <rect x="2" y="0" width="136" height="283" rx="18" fill="var(--phone-body)"/>
    <rect x="9" y="7" width="122" height="269" rx="12" fill="var(--teal)"/>
    <path d="M36 8 h68 v4 a4 4 0 0 1 -4 4 h-60 a4 4 0 0 1 -4 -4 z" fill="var(--phone-body)"/>
  </svg>
  <div class="phone-screen-text">
    <div class="phone-brand">Swift Tee</div>
    <div class="phone-tagline">
      <span class="big">Mobile</span>
      <span class="small">Payments</span>
      <span class="small">Method</span>
    </div>
  </div>

  <ul class="values">
    <li><svg viewBox="0 0 34 26" aria-hidden="true"><path d="M4 14 L13 22 L30 3" fill="none" stroke="var(--white)" stroke-width="4" stroke-linecap="round" stroke-linejoin="round"/></svg>Quick and easy</li>
    <li><svg viewBox="0 0 34 26" aria-hidden="true"><path d="M4 14 L13 22 L30 3" fill="none" stroke="var(--white)" stroke-width="4" stroke-linecap="round" stroke-linejoin="round"/></svg>Formal and polite</li>
    <li><svg viewBox="0 0 34 26" aria-hidden="true"><path d="M4 14 L13 22 L30 3" fill="none" stroke="var(--white)" stroke-width="4" stroke-linecap="round" stroke-linejoin="round"/></svg>Fun with professional boundary</li>
    <li><svg viewBox="0 0 34 26" aria-hidden="true"><path d="M4 14 L13 22 L30 3" fill="none" stroke="var(--white)" stroke-width="4" stroke-linecap="round" stroke-linejoin="round"/></svg>Mate-ship relationships</li>
    <li><svg viewBox="0 0 34 26" aria-hidden="true"><path d="M4 14 L13 22 L30 3" fill="none" stroke="var(--white)" stroke-width="4" stroke-linecap="round" stroke-linejoin="round"/></svg>100% online digital</li>
  </ul>

  <div class="brand-mark">Swift Tee</div>

  <p class="visit">Visit us at: swifttee.com.au</p>
</main>
</body>
</html>
```